Sherwood Ads

Would like to have new web ads announcing opening of a new pediatric office (Bramblefield Pediatrics - Sherwood). First and only dedicated pediatric clinic in Sherwood. Ads need to be following sizes: 160x160, 180x180, 300x250, 336x280, 728x90, 920x250, 1080x1080, 1200x627. Sample of previous ad attached.

```html
<!DOCTYPE html>
<html lang="en">
<head>
<meta charset="utf-8">
<title>Bramblefield Pediatrics – Sherwood Web Ads</title>
<link href="https://fonts.googleapis.com/css2?family=Montserrat:wght@400;700;800&family=Roboto:wght@400;700&display=swap" rel="stylesheet">
<style>
:root{
  --red:#e8321f;
  --blue:#1f44a0;
  --yellow:#f6d633;
  --ink:#222;
  --board:#dcdcdc;
  --white:#fff;
  --photo:linear-gradient(125deg,#efe0bd 0%,#c99d68 30%,#8a6a4a 55%,#4f6b6c 80%,#3a4858 100%);
}
*{margin:0;padding:0;box-sizing:border-box}
html,body{width:1200px;height:782px;overflow:hidden;background:var(--board)}
body{position:relative;font-family:"Roboto",Arial,sans-serif;color:var(--ink)}
.ad{position:absolute;background:var(--white);overflow:hidden}
.photo{position:absolute;background:var(--photo)}
.wave{position:absolute;left:0;width:100%;display:block}
.dot{position:absolute;border-radius:50%}
.dot.red{background:var(--red)}
.dot.blue{background:var(--blue)}
.dot.yellow{background:var(--yellow)}
.head{position:absolute;left:0;right:0;text-align:center}
.h-red{font-family:"Montserrat",sans-serif;font-weight:800;color:var(--red);line-height:1.05;white-space:nowrap}
.h-blue{font-family:"Montserrat",sans-serif;font-weight:400;color:var(--blue);line-height:1.1;white-space:nowrap}
.h-blue b{font-weight:800}
.welcome{font-family:"Roboto",Arial,sans-serif;line-height:1.15;color:var(--ink);white-space:nowrap}
.welcome b{font-weight:700}
.services{position:absolute;left:0;right:0;text-align:center;font-family:"Montserrat",sans-serif;font-weight:700;color:var(--red);line-height:1.12;white-space:nowrap}
.brand{position:absolute;display:flex;align-items:center}
.brand-mark{border-radius:50%;background:var(--blue);flex:none}
.brand-name{font-family:"Montserrat",sans-serif;font-weight:700;color:var(--blue);line-height:1;white-space:nowrap}
.cta{position:absolute;display:flex;align-items:center;justify-content:center;background:var(--red);color:var(--white);border-radius:999px;font-family:"Montserrat",sans-serif;font-weight:700;white-space:nowrap}

/* square ads: base 256px, scaled by --s */
.sq{width:calc(256px*var(--s));height:calc(256px*var(--s))}
.sq .head{top:calc(7px*var(--s))}
.sq .h-red{font-size:calc(16.5px*var(--s))}
.sq .h-blue{font-size:calc(13.5px*var(--s))}
.sq .welcome{font-size:calc(8.3px*var(--s));margin-top:calc(4px*var(--s))}
.sq .photo{left:0;right:0;top:calc(54px*var(--s));height:calc(122px*var(--s))}
.sq .wave{top:calc(128px*var(--s));height:calc(50px*var(--s))}
.sq .services{top:calc(177px*var(--s));font-size:calc(12.5px*var(--s))}
.sq .red{left:calc(9px*var(--s));top:calc(160px*var(--s));width:calc(13px*var(--s));height:calc(13px*var(--s))}
.sq .blue{left:calc(10px*var(--s));top:calc(181px*var(--s));width:calc(6px*var(--s));height:calc(6px*var(--s))}
.sq .yellow{left:calc(238px*var(--s));top:calc(208px*var(--s));width:calc(9px*var(--s));height:calc(9px*var(--s))}
.sq .brand{left:calc(16px*var(--s));top:calc(224px*var(--s));gap:calc(6px*var(--s))}
.sq .brand-mark{width:calc(24px*var(--s));height:calc(24px*var(--s))}
.sq .brand-name{font-size:calc(11px*var(--s))}
.sq .cta{left:calc(166px*var(--s));top:calc(226px*var(--s));width:calc(77px*var(--s));height:calc(20px*var(--s));font-size:calc(9.5px*var(--s))}

/* small rectangle ads: base 228x190, scaled by --s */
.rc{width:calc(228px*var(--s));height:calc(190px*var(--s))}
.rc .head{top:calc(6px*var(--s))}
.rc .h-red{font-size:calc(14px*var(--s))}
.rc .h-blue{font-size:calc(11.2px*var(--s))}
.rc .welcome{font-size:calc(6.8px*var(--s));margin-top:calc(3px*var(--s))}
.rc .photo{left:0;right:0;top:calc(44px*var(--s));height:calc(100px*var(--s))}
.rc .wave{top:calc(106px*var(--s));height:calc(42px*var(--s))}
.rc .services{top:calc(131px*var(--s));font-size:calc(10.6px*var(--s))}
.rc .red{left:calc(10px*var(--s));top:calc(121px*var(--s));width:calc(10px*var(--s));height:calc(10px*var(--s))}
.rc .blue{left:calc(12px*var(--s));top:calc(137px*var(--s));width:calc(4px*var(--s));height:calc(4px*var(--s))}
.rc .yellow{left:calc(208px*var(--s));top:calc(146px*var(--s));width:calc(9px*var(--s));height:calc(9px*var(--s))}
.rc .brand{left:calc(15px*var(--s));top:calc(163px*var(--s));gap:calc(5px*var(--s))}
.rc .brand-mark{width:calc(19px*var(--s));height:calc(19px*var(--s))}
.rc .brand-name{font-size:calc(8.5px*var(--s))}
.rc .cta{left:calc(156px*var(--s));top:calc(168px*var(--s));width:calc(58px*var(--s));height:calc(14px*var(--s));font-size:calc(7px*var(--s))}

.ad-300{left:269px;top:483px;--s:1}
.ad-336{left:548px;top:483px;--s:1}
.ad-1080{left:827px;top:397px;--s:1.336}
.ad-180{left:27px;top:341px;--s:0.974}
.ad-160{left:27px;top:549px;--s:1}

/* 1200x627 */
.ad-1200{left:27px;top:34px;width:534px;height:279px}
.ad-1200 .photo{left:220px;top:0;right:0;bottom:0}
.ad-1200 .curve{position:absolute;left:220px;top:0;width:60px;height:279px}
.ad-1200 .head{left:16px;right:310px;top:14px}
.ad-1200 .h-red{font-size:24px;line-height:.92}
.ad-1200 .h-blue{font-size:20px;line-height:1}
.ad-1200 .h-blue.big{font-size:22px}
.ad-1200 .welcome{font-size:11.5px;margin-top:6px}
.ad-1200 .rule{position:absolute;left:50px;width:130px;top:158px;height:1px;background:#eee}
.ad-1200 .services{left:10px;right:290px;top:166px;font-size:14px}
.ad-1200 .red{left:14px;top:115px;width:14px;height:14px}
.ad-1200 .blue{left:14px;top:134px;width:6px;height:6px}
.ad-1200 .yellow{left:211px;top:210px;width:15px;height:15px}
.ad-1200 .brand{left:20px;top:232px;gap:8px}
.ad-1200 .brand-mark{width:30px;height:30px}
.ad-1200 .brand-name{font-size:12.5px}
.ad-1200 .cta{left:165px;top:234px;width:101px;height:27px;font-size:13px}

/* 728x90 */
.ad-728{left:575px;top:259px;width:422px;height:53px}
.ad-728 .photo{left:182px;width:118px;top:0;bottom:0}
.ad-728 .head{left:10px;right:240px;top:7px}
.ad-728 .h-red{font-size:11px}
.ad-728 .h-blue{font-size:9.8px}
.ad-728 .welcome{font-size:6.3px;margin-top:2px}
.ad-728 .services{left:300px;right:0;top:8px;font-size:6.5px}
.ad-728 .red{left:8px;top:5px;width:7px;height:7px}
.ad-728 .yellow.y1{left:8px;top:15px;width:4px;height:4px}
.ad-728 .blue{left:172px;top:40px;width:6px;height:6px}
.ad-728 .yellow.y2{left:410px;top:27px;width:5px;height:5px}
.ad-728 .brand{left:312px;top:33px;gap:3px}
.ad-728 .brand-mark{width:11px;height:11px}
.ad-728 .brand-name{font-size:5.2px}
.ad-728 .cta{left:366px;top:34px;width:40px;height:9px;font-size:5px}

/* 920x250 */
.ad-920{left:269px;top:325px;width:533px;height:145px}
.ad-920 .photo{left:350px;right:0;top:0;bottom:0}
.ad-920 .curve{position:absolute;left:345px;top:0;width:40px;height:145px}
.ad-920 .head{left:0;right:185px;top:8px}
.ad-920 .h-red{font-size:21px}
.ad-920 .h-blue{font-size:17.5px}
.ad-920 .welcome{font-size:11px;margin-top:5px}
.ad-920 .services{left:0;right:160px;top:90px;font-size:12.5px}
.ad-920 .red{left:23px;top:62px;width:16px;height:16px}
.ad-920 .blue{left:18px;top:82px;width:7px;height:7px}
.ad-920 .yellow{left:327px;top:95px;width:17px;height:17px}
.ad-920 .brand{left:15px;top:115px;gap:6px}
.ad-920 .brand-mark{width:20px;height:20px}
.ad-920 .brand-name{font-size:9.5px}
.ad-920 .cta{left:277px;top:118px;width:70px;height:17px;font-size:9px}
</style>
</head>
<body>

<section class="ad ad-1200">
  <div class="photo" role="img" aria-label="Photo of a group of smiling children outdoors in warm sunlight"></div>
  <svg class="curve" viewBox="0 0 60 279" preserveAspectRatio="none" aria-hidden="true"><path d="M0 0H42C22 50 18 100 34 150S46 240 28 279H0Z" fill="#fff"/></svg>
  <div class="head">
    <div class="h-red">NEW CLINIC</div>
    <div class="h-red">— COMING —</div>
    <div class="h-blue big"><b>TO SHERWOOD,</b></div>
    <div class="h-blue">OR IN JULY 2026</div>
    <p class="welcome">Welcoming <b>New Patients</b><br>With Same-day<br>Appointments Available</p>
  </div>
  <span class="dot red"></span><span class="dot blue"></span><span class="dot yellow"></span>
  <div class="rule"></div>
  <div class="services">Behavioral Health | Telehealth<br>Pediatric Primary Care</div>
  <div class="brand"><span class="brand-mark"></span><span class="brand-name">Bramblefield<br>Pediatrics</span></div>
  <div class="cta">Book A Visit</div>
</section>

<section class="ad ad-728">
  <div class="photo" role="img" aria-label="Photo of a group of smiling children outdoors"></div>
  <div class="head">
    <div class="h-red">— NEW CLINIC COMING —</div>
    <div class="h-blue"><b>TO SHERWOOD,</b> OR IN JULY 2026</div>
    <p class="welcome">Welcoming <b>New Patients</b> With Same-day<br>Appointments Available</p>
  </div>
  <span class="dot red"></span><span class="dot yellow y1"></span><span class="dot blue"></span><span class="dot yellow y2"></span>
  <div class="services">Behavioral Health | Telehealth<br>Pediatric Primary Care</div>
  <div class="brand"><span class="brand-mark"></span><span class="brand-name">Bramblefield<br>Pediatrics</span></div>
  <div class="cta">Book A Visit</div>
</section>

<section class="ad ad-920">
  <div class="photo" role="img" aria-label="Photo of a group of smiling children outdoors in warm sunlight"></div>
  <svg class="curve" viewBox="0 0 40 145" preserveAspectRatio="none" aria-hidden="true"><path d="M0 0H28C12 30 8 60 20 85S30 125 14 145H0Z" fill="#fff"/></svg>
  <div class="head">
    <div class="h-red">— NEW CLINIC COMING —</div>
    <div class="h-blue"><b>TO SHERWOOD,</b> OR IN JULY 2026</div>
    <p class="welcome">Welcoming <b>New Patients</b> With Same-day<br>Appointments Available</p>
  </div>
  <span class="dot red"></span><span class="dot blue"></span><span class="dot yellow"></span>
  <div class="services">Behavioral Health | Telehealth<br>Pediatric Primary Care</div>
  <div class="brand"><span class="brand-mark"></span><span class="brand-name">Bramblefield<br>Pediatrics</span></div>
  <div class="cta">Book A Visit</div>
</section>

<section class="ad rc ad-180">
  <div class="photo" role="img" aria-label="Photo of a group of smiling children outdoors"></div>
  <svg class="wave" viewBox="0 0 100 30" preserveAspectRatio="none" aria-hidden="true"><path d="M0 24C20 12 40 6 60 12S88 22 100 10V30H0Z" fill="#fff"/></svg>
  <div class="head">
    <div class="h-red">— NEW CLINIC COMING —</div>
    <div class="h-blue"><b>TO SHERWOOD,</b> OR IN JULY 2026</div>
    <p class="welcome">Welcoming <b>New Patients</b> With Same-day<br>Appointments Available</p>
  </div>
  <div class="services">Behavioral Health | Telehealth<br>Pediatric Primary Care</div>
  <div class="brand"><span class="brand-mark"></span><span class="brand-name">Bramblefield<br>Pediatrics</span></div>
  <div class="cta">Book A Visit</div>
</section>

<section class="ad rc ad-160">
  <div class="photo" role="img" aria-label="Photo of a group of smiling children outdoors"></div>
  <svg class="wave" viewBox="0 0 100 30" preserveAspectRatio="none" aria-hidden="true"><path d="M0 24C20 12 40 6 60 12S88 22 100 10V30H0Z" fill="#fff"/></svg>
  <div class="head">
    <div class="h-red">— NEW CLINIC COMING —</div>
    <div class="h-blue"><b>TO SHERWOOD,</b> OR IN JULY 2026</div>
    <p class="welcome">Welcoming <b>New Patients</b> With Same-day<br>Appointments Available</p>
  </div>
  <span class="dot red"></span><span class="dot blue"></span><span class="dot yellow"></span>
  <div class="services">Behavioral Health | Telehealth<br>Pediatric Primary Care</div>
  <div class="brand"><span class="brand-mark"></span><span class="brand-name">Bramblefield<br>Pediatrics</span></div>
  <div class="cta">Book A Visit</div>
</section>

<section class="ad sq ad-300">
  <div class="photo" role="img" aria-label="Photo of a group of smiling children outdoors in warm sunlight"></div>
  <svg class="wave" viewBox="0 0 100 30" preserveAspectRatio="none" aria-hidden="true"><path d="M0 24C20 12 40 6 60 12S88 22 100 10V30H0Z" fill="#fff"/></svg>
  <div class="head">
    <div class="h-red">— NEW CLINIC COMING —</div>
    <div class="h-blue"><b>TO SHERWOOD,</b> OR IN JULY 2026</div>
    <p class="welcome">Welcoming <b>New Patients</b> With Same-day<br>Appointments Available</p>
  </div>
  <span class="dot red"></span><span class="dot blue"></span><span class="dot yellow"></span>
  <div class="services">Behavioral Health | Telehealth<br>Pediatric Primary Care</div>
  <div class="brand"><span class="brand-mark"></span><span class="brand-name">Bramblefield<br>Pediatrics</span></div>
  <div class="cta">Book A Visit</div>
</section>

<section class="ad sq ad-336">
  <div class="photo" role="img" aria-label="Photo of a group of smiling children outdoors in warm sunlight"></div>
  <svg class="wave" viewBox="0 0 100 30" preserveAspectRatio="none" aria-hidden="true"><path d="M0 24C20 12 40 6 60 12S88 22 100 10V30H0Z" fill="#fff"/></svg>
  <div class="head">
    <div class="h-red">— NEW CLINIC COMING —</div>
    <div class="h-blue"><b>TO SHERWOOD,</b> OR IN JULY 2026</div>
    <p class="welcome">Welcoming <b>New Patients</b> With Same-day<br>Appointments Available</p>
  </div>
  <span class="dot red"></span><span class="dot blue"></span><span class="dot yellow"></span>
  <div class="services">Behavioral Health | Telehealth<br>Pediatric Primary Care</div>
  <div class="brand"><span class="brand-mark"></span><span class="brand-name">Bramblefield<br>Pediatrics</span></div>
  <div class="cta">Book A Visit</div>
</section>

<section class="ad sq ad-1080">
  <div class="photo" role="img" aria-label="Photo of a group of smiling children outdoors in warm sunlight"></div>
  <svg class="wave" viewBox="0 0 100 30" preserveAspectRatio="none" aria-hidden="true"><path d="M0 24C20 12 40 6 60 12S88 22 100 10V30H0Z" fill="#fff"/></svg>
  <div class="head">
    <div class="h-red">— NEW CLINIC COMING —</div>
    <div class="h-blue"><b>TO SHERWOOD,</b> OR IN JULY 2026</div>
    <p class="welcome">Welcoming <b>New Patients</b> With Same-day<br>Appointments Available</p>
  </div>
  <span class="dot red"></span><span class="dot blue"></span><span class="dot yellow"></span>
  <div class="services">Behavioral Health | Telehealth<br>Pediatric Primary Care</div>
  <div class="brand"><span class="brand-mark"></span><span class="brand-name">Bramblefield<br>Pediatrics</span></div>
  <div class="cta">Book A Visit</div>
</section>

</body>
</html>
```